Needing a business Card for new fire company.

Dalvo, sales fire equipment and parts. We also do tree clearing for the forest service. My logo will be attached to this. I am also looking for a design that when people see the card it stick with them and they will remember my sales team giving it to them.

```html
<!DOCTYPE html>
<html lang="en">
<head>
<meta charset="utf-8">
<title>Dalvo Business Card</title>
<link rel="stylesheet" href="https://fonts.googleapis.com/css2?family=Archivo+Black&family=Questrial&display=swap">
<style>
  :root {
    --page: #ffffff;
    --card-light: #ffffff;
    --card-dark: #060808;
    --fire-red: #c1272d;
    --ink: #0b0b0b;
    --paper-white: #ffffff;
  }
  * { margin: 0; padding: 0; box-sizing: border-box; }
  html, body {
    width: 1200px;
    height: 1168px;
    overflow: hidden;
    background: var(--page);
  }
  .canvas {
    position: relative;
    width: 1200px;
    height: 1168px;
  }
  .card {
    position: absolute;
    overflow: hidden;
  }
  .card--front {
    left: 204px;
    top: 151px;
    width: 701px;
    height: 410px;
    background: var(--card-light);
    box-shadow: 0 0 0 1px #ececec;
  }
  .card--back {
    left: 290px;
    top: 602px;
    width: 714px;
    height: 418px;
    background: var(--card-dark);
  }
  .brand {
    position: absolute;
    display: flex;
    align-items: center;
    gap: 12px;
    font-family: "Questrial", sans-serif;
    font-size: 62px;
    line-height: 1;
    letter-spacing: 2px;
  }
  .brand__dot {
    width: 22px;
    height: 22px;
    border-radius: 50%;
    background: var(--fire-red);
    flex: none;
  }
  .card--front .brand {
    left: 43px;
    top: 76px;
    color: var(--ink);
  }
  .card--back .brand {
    left: 0;
    right: 0;
    top: 150px;
    justify-content: center;
    color: var(--paper-white);
  }
  .person {
    position: absolute;
    left: 438px;
    width: 200px;
    top: 92px;
    text-align: center;
  }
  .person__name {
    font-family: "Archivo Black", sans-serif;
    font-size: 21px;
    letter-spacing: 1.5px;
    color: var(--ink);
    line-height: 1.2;
  }
  .person__role {
    font-family: "Questrial", sans-serif;
    font-size: 15px;
    letter-spacing: 1px;
    color: var(--fire-red);
    margin-top: 3px;
  }
  .contact {
    position: absolute;
    left: 44px;
    top: 220px;
    list-style: none;
    font-family: "Questrial", sans-serif;
    font-size: 17px;
    color: var(--ink);
    letter-spacing: 0.5px;
  }
  .contact__item {
    display: flex;
    align-items: flex-start;
    height: 26px;
  }
  .contact__item--address { height: 48px; line-height: 22px; }
  .contact__icon {
    width: 18px;
    height: 18px;
    margin-right: 9px;
    margin-top: 2px;
    flex: none;
  }
  .flame-art {
    position: absolute;
    left: 296px;
    top: 169px;
    width: 405px;
    height: 241px;
  }
  .tool-rule {
    position: absolute;
    left: 0;
    top: 340px;
    width: 714px;
    height: 30px;
  }
</style>
</head>
<body>
<main class="canvas">

  <section class="card card--front" aria-label="Card front">
    <div class="brand"><span class="brand__dot"></span><span class="brand__name">Dalvo</span></div>

    <div class="person">
      <p class="person__name">XXXXXX XXXXX</p>
      <p class="person__role">XXXXXX XXX</p>
    </div>

    <ul class="contact">
      <li class="contact__item">
        <svg class="contact__icon" viewBox="0 0 20 20"><path fill="#c1272d" d="M2 7c0-2 4-3 8-3s8 1 8 3v2h-4V7.5c-1-.5-3-.6-4-.6s-3 .1-4 .6V9H2z M5 10l2-2h6l2 2v6H5z"/></svg>
        <span>(xxx) xxx-xxxx</span>
      </li>
      <li class="contact__item">
        <svg class="contact__icon" viewBox="0 0 20 20"><rect x="1" y="4" width="18" height="12" fill="#c1272d"/><path d="M1 4l9 7 9-7" fill="none" stroke="#fff" stroke-width="1.5"/></svg>
        <span>xxxxx@xxxxxxxxx.com</span>
      </li>
      <li class="contact__item contact__item--address">
        <svg class="contact__icon" viewBox="0 0 20 20"><path fill="#c1272d" d="M10 1a6.5 6.5 0 0 0-6.5 6.5C3.5 12 10 19 10 19s6.5-7 6.5-11.5A6.5 6.5 0 0 0 10 1zm0 9a2.5 2.5 0 1 1 0-5 2.5 2.5 0 0 1 0 5z"/></svg>
        <span>xxxx x. xxxx xxxxx<br>xxxxxx, xxx xxxx</span>
      </li>
      <li class="contact__item">
        <svg class="contact__icon" viewBox="0 0 20 20" fill="none" stroke="#c1272d" stroke-width="1.3"><circle cx="10" cy="10" r="8"/><ellipse cx="10" cy="10" rx="3.5" ry="8"/><path d="M2 10h16M3.5 6h13M3.5 14h13"/></svg>
        <span>www.xxxxxxxxxxxx.com</span>
      </li>
    </ul>

    <svg class="flame-art" role="img" aria-label="Red flame illustration rising from the bottom right corner" viewBox="0 0 405 241" preserveAspectRatio="none">
      <defs>
        <linearGradient id="flameFade" x1="0" y1="1" x2="0.6" y2="0">
          <stop offset="0" stop-color="#c1272d"/>
          <stop offset="1" stop-color="#c1272d" stop-opacity="0.15"/>
        </linearGradient>
      </defs>
      <rect width="405" height="241" fill="url(#flameFade)"/>
    </svg>
  </section>

  <section class="card card--back" aria-label="Card back">
    <div class="brand"><span class="brand__dot"></span><span class="brand__name">Dalvo</span></div>

    <svg class="tool-rule" viewBox="0 0 714 30" aria-label="Fire equipment icons">
      <rect x="0" y="12" width="271" height="6" fill="#c1272d"/>
      <rect x="442" y="12" width="272" height="6" fill="#c1272d"/>
      <g fill="#fff">
        <circle cx="295" cy="15" r="14"/>
        <circle cx="336" cy="15" r="14"/>
        <circle cx="377" cy="15" r="14"/>
        <circle cx="419" cy="15" r="14"/>
      </g>
      <g fill="#060808">
        <rect x="293" y="6" width="3" height="19"/>
        <rect x="330" y="7" width="12" height="4"/><rect x="335" y="7" width="3" height="18"/>
        <rect x="373" y="9" width="8" height="16" rx="3"/>
        <path d="M414 6h10l-2 9h-6z"/><rect x="418" y="14" width="2" height="11"/>
      </g>
    </svg>
  </section>

</main>
</body>
</html>
```